Email Marketing Campaign 50% discount and buy-2-get-1 offer

I would like to inform my customers of our special offers via a e-Newsletter/Marketing E-Mail.

The coding needs to be done by the designer.

I have most of the design and the message that we wish to convey our buyers.

The information is:

1. We have now 50% discount on all our carpets

2. We have a buy-2 get-1 free carpet offer

For both the above messages we have already banner style that we like to use in our Newsletter.
I have attached the banner and the designers can use it.

3. We have opened a new shop in Berlin Germany

Therefore we like to have a Sylish Newsletter design that fits our website and products using the banner idea and we wish to include the 3 messages.
Special note should be given that this newsletter is going to our previous buyers. Therefore they already know us, and we just like to inform them of our latest news and offer.

Target Market(s)

Upmarket buyers looking for a great deal

Industry/Entity Type

Marketing

Coding

Coded - Design and coding required

Number of Pages Required

1 page

Font styles to use
Sans Serif

Colors
e667a6
34a7d8

Requirements
Must have
• Clear explanation with excitement in the message
Nice to have
• To promote clearly the 3 for 2 with maybe an explanation and clear images describing what the promotion is and how it works.
• I.e. buy 2 get 1 extra carpet of your choice free
• Add carpets to checkout and the system will calculate automatically
• The lowest carpet in your selection of 3 is the free carpet

```html
<!DOCTYPE html>
<html lang="en">
<head>
<meta charset="utf-8">
<title>Heritage Rugs – Biggest Carpet Sale of the Year</title>
<link rel="stylesheet" href="https://fonts.googleapis.com/css2?family=Libre+Baskerville:wght@400;700&family=Roboto:wght@400;500;700&display=swap">
<style>
  :root{
    --frame:#333333;
    --paper:#ffffff;
    --notice:#5bb31e;
    --ink:#1f1f24;
    --muted:#555555;
    --pink:#e667a6;
    --magenta:#d8327f;
    --blue:#34a7d8;
    --orange:#f7901e;
    --peach-band:#f3a77c;
    --peach-fill:#fcd6c1;
    --pale:#f3f5f9;
    --rule:#dddddd;
  }
  *{margin:0;padding:0;box-sizing:border-box}
  html,body{width:1200px;height:3067px;overflow:hidden}
  body{background:var(--frame);font-family:"Roboto",Arial,sans-serif;color:var(--ink);position:relative}
  .abs{position:absolute}
  .notice-bar{left:46px;top:20px;width:1108px;height:85px;background:var(--notice);color:#fff;
    font-size:27px;display:flex;align-items:center;justify-content:center;gap:8px}
  .notice-bar b{font-weight:700}
  .sheet{left:46px;top:187px;width:1108px;height:2844px;background:var(--paper)}
  .logo-tab{left:345px;top:150px;width:520px;height:290px}
  .logo-name{left:355px;top:220px;width:500px;text-align:center;font-family:"Libre Baskerville",Georgia,serif;
    font-size:58px;font-weight:400;color:#8a8a8f;letter-spacing:2px}
  .centered{left:46px;width:1108px;text-align:center}
  .headline{font-family:"Libre Baskerville",Georgia,serif;font-weight:700;font-size:63px;letter-spacing:0;line-height:1}
  .subline{display:flex;align-items:center;justify-content:center;gap:28px;font-family:"Libre Baskerville",Georgia,serif;
    font-weight:700;font-size:38px;letter-spacing:2px;color:#3a3a44}
  .subline::before,.subline::after{content:"";width:130px;height:3px;background:#3a3a44}
  .hero{left:82px;top:631px;width:1036px;height:724px;
    background:linear-gradient(135deg,#cfc9bf 0%,#b8b0a4 35%,#6d5f5a 65%,#4a3d40 100%)}
  .offer{left:99px;top:655px;width:354px;height:298px;background:rgba(214,70,140,.9);
    border:4px solid rgba(255,255,255,.9);box-shadow:0 0 0 3px rgba(214,70,140,.9);color:#fff;text-align:center;padding-top:16px;overflow:hidden}
  .offer .big{font-size:122px;font-weight:700;line-height:1;display:inline-flex;align-items:flex-start}
  .offer .big small{display:flex;flex-direction:column;font-size:42px;line-height:1.05;margin-left:8px;margin-top:12px}
  .offer .line{font-size:30px;line-height:1.2;margin-top:10px}
  .offer .extra{font-size:32px;line-height:1.2;font-weight:700;color:#1f1f24;margin-top:4px}
  .offer .valid{font-size:24px;line-height:1.2;color:#ffe067;margin-top:8px}
  .deal{left:82px;top:1572px;width:1036px;height:532px;background:var(--pale)}
  .tag{height:80px;color:#fff;font-size:50px;font-weight:500;display:flex;align-items:center;justify-content:center}
  .tag.buy{left:312px;top:1601px;width:148px;background:var(--orange)}
  .tag.free{left:819px;top:1601px;width:204px;background:var(--magenta)}
  .bracket{left:171px;top:1638px;width:427px;height:40px;border:3px solid var(--orange);border-bottom:none}
  .rug{width:264px;height:264px;border-radius:50%;border:9px solid #fff;box-shadow:0 6px 14px rgba(0,0,0,.25)}
  .rug.one{left:131px;top:1742px;background:radial-gradient(circle,#6a5a68,#2c2a33 70%)}
  .rug.two{left:460px;top:1742px;background:radial-gradient(circle,#c98a6e,#a85b4d 60%,#6f3e44)}
  .rug.three{left:828px;top:1742px;background:radial-gradient(circle,#e6b0a8,#d49495 60%,#c07c80)}
  .shop-band{left:46px;top:2131px;width:1108px;height:283px;background:var(--peach-band);padding:13px}
  .shop-band .inner{width:100%;height:100%;background:var(--peach-fill)}
  .shop-icon{left:112px;top:2160px;width:230px;height:230px;background:linear-gradient(180deg,#e23d8f,#b4206a);border-radius:10px}
  .shop-kicker{left:418px;top:2200px;font-size:40px;color:var(--orange);letter-spacing:0;white-space:nowrap}
  .shop-city{left:418px;top:2250px;font-family:"Libre Baskerville",Georgia,serif;font-weight:700;font-size:56px;color:var(--ink);white-space:nowrap}
  .shop-city span{color:var(--magenta)}
  .shop-address{left:420px;top:2334px;font-size:27px;color:#222;white-space:nowrap}
  .foot-head{font-size:27px;font-weight:700;letter-spacing:1px}
  .foot-text{font-size:27px;line-height:49px;color:#222}
  .foot-text a{color:var(--blue);text-decoration:none}
  .rule{height:2px;background:var(--rule)}
  .social{top:2752px;width:98px;height:98px;border-radius:50%}
  .small-print{font-size:23px;color:#555;letter-spacing:1px}
</style>
</head>
<body>
  <div class="abs notice-bar">Having trouble seeing this mail?<b>Click here.</b> Don't want to receive this?<b>Unsubscribe</b></div>

  <div class="abs sheet"></div>

  <svg class="abs logo-tab" viewBox="0 0 520 290" aria-hidden="true">
    <defs><filter id="tabShadow" x="-10%" y="-10%" width="120%" height="130%"><feDropShadow dx="0" dy="3" stdDeviation="5" flood-opacity=".25"/></filter></defs>
    <path d="M10 5 H510 V210 L260 280 L10 210 Z" fill="#fff" filter="url(#tabShadow)"/>
  </svg>
  <div class="abs logo-name">Heritage Rugs</div>

  <h1 class="abs centered headline" style="top:468px">BIGGEST CARPET SALE</h1>
  <div class="abs centered subline" style="top:548px">OF THE YEAR</div>

  <div class="abs hero" role="img" aria-label="Living room with a white sofa, glass coffee table and a large faded vintage carpet"></div>
  <div class="abs offer">
    <div class="big">50<small><span>OFF</span><span>%</span></small></div>
    <div class="line">Buy One Carpet &amp; Get</div>
    <div class="extra">EXTRA 50% OFF</div>
    <div class="valid">Offer Valid for All Carpets</div>
  </div>

  <h2 class="abs centered headline" style="top:1414px">3 FOR 2 COUPON</h2>
  <div class="abs centered subline" style="top:1510px">BUY 2 GET 1 FREE</div>

  <div class="abs deal"></div>
  <div class="abs bracket"></div>
  <div class="abs tag buy">BUY 2</div>
  <div class="abs tag free">1 FREE</div>
  <div class="abs rug one" role="img" aria-label="Dark grey and plum vintage carpet"></div>
  <div class="abs rug two" role="img" aria-label="Terracotta medallion vintage carpet"></div>
  <div class="abs rug three" role="img" aria-label="Soft pink overdyed vintage carpet, the free choice"></div>

  <div class="abs shop-band"><div class="inner"></div></div>
  <div class="abs shop-icon" role="img" aria-label="Shop front with striped awning"></div>
  <div class="abs shop-kicker">WE HAVE OPENED A NEW SHOP</div>
  <div class="abs shop-city"><span>BERLIN</span>, GERMANY</div>
  <div class="abs shop-address">Sample street 21, Phone No:&nbsp; +44 203 000 4417</div>

  <div class="abs foot-head" style="left:105px;top:2474px">HERITAGE RUGS</div>
  <div class="abs foot-text" style="left:105px;top:2518px">14 Marlow Terrace<br>and Elmside Road<br>Athens Greece 10550<br>EL 104662390</div>
  <div class="abs foot-head" style="left:717px;top:2474px">CONTACT</div>
  <div class="abs foot-text" style="left:717px;top:2518px">Telephone: <a href="#">+44 203 000 4417</a><br>Email: <a href="#">hello@heritagerugs.example</a></div>

  <div class="abs rule" style="left:273px;top:2728px;width:730px"></div>
  <div class="abs social" style="left:336px;background:#b32121"></div>
  <div class="abs social" style="left:441px;background:#c9252c"></div>
  <div class="abs social" style="left:549px;background:#3b5a99"></div>
  <div class="abs social" style="left:658px;background:#f4a33a"></div>
  <div class="abs social" style="left:766px;background:#1aaae3"></div>
  <div class="abs rule" style="left:273px;top:2874px;width:730px"></div>

  <div class="abs centered small-print" style="top:2906px">© 2016, ALL RIGHTS RESERVED</div>
  <div class="abs centered small-print" style="top:2964px">unsubscribe from this list &nbsp;|&nbsp; update subscription preferences</div>
</body>
</html>
```